New website design for small car detailing company.

We have a small cleaning company, our main focus is car detailing but we are also expanding to home and residential cleaning and power washing.
I would like the web site to have a simple layout and SEO friendly.
I would also like to have a contact page in which clients can contact us and upload pictures of the house or car so we can provide an estimate.
A Page that shows the services we offer.

Target Market(s)

High paying clients for car detailiing and focus on residential and commercial cleaning.

Industry/Entity Type

Cleaning Service

Coding

Coded - Design and coding required

Number of Pages Required

4 page

Font styles to use
Serif

Colors

Designer to choose only greyscale colors for use in the design.

Requirements
Must have
• A home page.
Blog page for SEO
Contact page with the choice of clients to upload theirs pictures so we can provide estimates with calendar integration so they can provide their available dates for service.
A pictures to sell our services.
Nice to have
• Simple but sleek desing, I am more interested in SEO Score than heavy loads

```html
<!DOCTYPE html>
<html lang="en">
<head>
<meta charset="utf-8">
<title>Pinecrest Mobile Detailing – Car Detailing</title>
<link href="https://fonts.googleapis.com/css2?family=Lora:wght@400;500;600;700&family=Playfair+Display:wght@600;700;800&display=swap" rel="stylesheet">
<style>
  :root{
    --stage:#d9dadc;
    --page:#ffffff;
    --panel:#141414;
    --ink:#111111;
    --nav-muted:#777777;
    --white:#ffffff;
    --accent-light:rgba(200,200,200,.82);
    --accent-mid:#a4a4a4;
    --soft-grey:#a9a9a9;
    --dim-grey:#858585;
    --display:"Playfair Display",serif;
    --text:"Lora",serif;
  }
  *{margin:0;padding:0;box-sizing:border-box}
  html,body{width:1200px;height:704px;overflow:hidden;background:var(--stage);font-family:var(--text)}
  .canvas{position:relative;width:1200px;height:704px}
  .page{position:absolute;left:32px;top:32px;width:869px;height:639px;background:var(--page)}
  .side-panel{position:absolute;left:901px;top:32px;width:267px;height:639px;background:var(--panel)}

  .brand{position:absolute;left:62px;top:68px;display:flex;align-items:center;gap:4px}
  .brand-dot{width:9px;height:9px;border-radius:50%;background:var(--ink)}
  .brand-name{font-size:7px;font-weight:700;line-height:1.15;color:var(--ink);width:44px}

  .main-nav{position:absolute;left:128px;top:74px;font-size:13px;font-weight:600}
  .main-nav a{text-decoration:none;color:var(--nav-muted);position:absolute;white-space:nowrap}
  .main-nav .is-active{color:var(--ink)}
  .main-nav .is-active::after{content:"";position:absolute;left:22px;top:18px;width:20px;height:1.5px;background:var(--ink)}

  .menu-toggle{position:absolute;left:846px;top:78px}

  .hero{position:absolute;left:128px;top:123px;width:686px;height:457px;overflow:hidden}
  .hero-photo{position:absolute;inset:0;
    background:
      radial-gradient(ellipse 17% 27% at 60% 58%,rgba(150,150,158,.75) 0%,rgba(110,112,120,.45) 55%,rgba(0,0,0,0) 100%),
      radial-gradient(ellipse 38% 35% at 72% 88%,rgba(175,176,184,.7) 0%,rgba(120,122,132,.35) 55%,rgba(0,0,0,0) 100%),
      radial-gradient(ellipse 22% 10% at 8% 45%,rgba(130,130,136,.45) 0%,rgba(0,0,0,0) 100%),
      linear-gradient(170deg,#4a4d57 0%,#24262d 30%,#1b1c22 60%,#34363d 85%,#6e7078 100%)}
  .slide-count{position:absolute;left:25px;top:220px;font-size:11px;font-weight:600;color:var(--white)}
  .hero-title{position:absolute;right:38px;top:26px;font-family:var(--display);font-size:21px;font-weight:700;color:var(--white);text-align:right;white-space:nowrap}
  .hero-copy{position:absolute;right:38px;top:56px;font-size:7.4px;line-height:9.2px;color:var(--white);text-align:right}
  .slider-arrows{position:absolute;left:112px;top:423px}
  .slider-dots{position:absolute;left:300px;top:429px;display:flex;gap:7px}
  .slider-dots span{width:24px;height:1.3px;background:rgba(255,255,255,.5)}
  .slider-dots .is-current{background:var(--white)}
  .hero-actions{position:absolute;left:478px;top:421px;display:flex}
  .btn{width:85px;height:20px;font-size:6px;display:flex;align-items:center;justify-content:center;text-decoration:none}
  .btn-solid{background:var(--white);color:var(--ink)}
  .btn-outline{border:1px solid var(--white);color:var(--white)}

  .next-card{position:absolute;left:176px;top:156px;width:124px;height:89px;display:flex}
  .next-card-arrow{width:38px;height:89px;background:var(--white);display:flex;align-items:center;justify-content:center}
  .next-card-photo{position:relative;width:86px;height:89px;background:linear-gradient(140deg,#45464b,#18191c 65%,#2c2d31)}
  .next-card-num{position:absolute;left:26px;top:28px;font-family:var(--display);font-size:25px;font-weight:700;color:var(--accent-mid);font-variant-numeric:lining-nums}

  .slide-number{position:absolute;left:88px;top:500px;font-family:var(--display);font-size:128px;font-weight:800;line-height:1;color:var(--accent-light);letter-spacing:-3px;font-variant-numeric:lining-nums}

  .panel-arrow{position:absolute;left:1023px;top:78px}
  .vertical{position:absolute;writing-mode:vertical-rl;transform:rotate(180deg);white-space:nowrap;font-family:var(--display)}
  .v-main{left:1010px;top:124px;height:256px;font-size:33px;font-weight:700;color:var(--white)}
  .v-sub{left:1018px;top:405px;height:108px;font-size:22px;font-weight:700;color:var(--soft-grey)}
  .v-home{left:1022px;top:537px;height:44px;font-size:13px;font-weight:700;color:var(--dim-grey)}
</style>
</head>
<body>
<div class="canvas">
  <div class="page"></div>
  <aside class="side-panel"></aside>

  <div class="brand">
    <span class="brand-dot"></span>
    <span class="brand-name">Pinecrest Mobile Detailing</span>
  </div>

  <nav class="main-nav">
    <a class="is-active" href="#" style="left:0">Home</a>
    <a href="#" style="left:86px">About Us</a>
    <a href="#" style="left:172px">Services</a>
    <a href="#" style="left:257px">Gallery</a>
  </nav>

  <svg class="menu-toggle" width="22" height="13" viewBox="0 0 22 13" aria-label="Menu">
    <g stroke="#111" stroke-width="1.2"><line x1="0" y1="1" x2="22" y2="1"/><line x1="0" y1="6.5" x2="22" y2="6.5"/><line x1="0" y1="12" x2="22" y2="12"/></g>
  </svg>

  <section class="hero">
    <div class="hero-photo" role="img" aria-label="Dark sports car being steam cleaned, mist rising around the front wheel"></div>
    <div class="slide-count">01/03</div>
    <h1 class="hero-title">Premium Cleaning Service</h1>
    <p class="hero-copy">Lorem ipsum dolor sit amet,<br>consectetur adipiscing elit,<br>sed do eiusmod tempor incididunt<br>ut labore et dolore magna aliqua.<br>Ut enim ad minim veniam.</p>
    <svg class="slider-arrows" width="62" height="12" viewBox="0 0 62 12" aria-label="Slide controls">
      <g stroke="#fff" stroke-width="1.2" fill="none">
        <line x1="1" y1="6" x2="26" y2="6"/><polyline points="6,1 1,6 6,11"/>
        <line x1="35" y1="6" x2="60" y2="6"/><polyline points="55,1 60,6 55,11"/>
      </g>
    </svg>
    <div class="slider-dots"><span class="is-current"></span><span></span><span></span></div>
    <div class="hero-actions">
      <a class="btn btn-solid" href="#">Find Out More</a>
      <a class="btn btn-outline" href="#">Order Now</a>
    </div>
  </section>

  <div class="next-card">
    <div class="next-card-arrow">
      <svg width="17" height="8" viewBox="0 0 17 8"><g stroke="#111" stroke-width="1.1" fill="none"><line x1="0" y1="4" x2="16" y2="4"/><polyline points="12.5,0.5 16,4 12.5,7.5"/></g></svg>
    </div>
    <div class="next-card-photo" role="img" aria-label="Gloved hand polishing a car headlight">
      <span class="next-card-num">02</span>
    </div>
  </div>

  <div class="slide-number">01</div>

  <svg class="panel-arrow" width="25" height="10" viewBox="0 0 25 10" aria-label="Next">
    <g stroke="#fff" stroke-width="1.2" fill="none"><line x1="0" y1="5" x2="24" y2="5"/><polyline points="20,1 24,5 20,9"/></g>
  </svg>
  <div class="vertical v-main">Car Detailing</div>
  <div class="vertical v-sub">Cleaning</div>
  <div class="vertical v-home">Home</div>
</div>
</body>
</html>
```